New label design for Vitmain Water beverage

This is to create a new label for a vitamin water company called Zelbo Vitamin. The label should be in dual languages. English and Arabic as seen attached for a previous example. You do not have to create an Arabic logo, just make space for it and I will have someon else do it. If you think you can do it, go ahead. I have also attached the bottle dimensions we are thinking of using. Please provide a new bottle design if you see fit. Please remember the bottle size is 400ml, and no pressure If I don't get a great bottle design, then I will use the attached one in that case. Please make the label diverse for various flavors, so it would apply easily and color print friendly. The brand is healthy, sporty, low or no sugars, no artificial flavors and no artificial coloring. All vitamins, minirals and electrolytes are healthy and real. Three flavors: pomogranite cherry, tropical citrus, and kiwi strawberry. So, each label would have different vitamins and offers unique components. Make it hip, trendy yet classy.
Good Luck!!!
Updates

Target Market(s)

Age 15-40 males and females

Industry/Entity Type

Water Company

Requirements
Nice to have
• Plastic PET bottle design
• a 500 ml version

```html
<!DOCTYPE html>
<html lang="en">
<head>
<meta charset="utf-8">
<title>Zelbo Vitamin – Label Design</title>
<link rel="stylesheet" href="https://fonts.googleapis.com/css2?family=Open+Sans:wght@400;700;800&family=Roboto+Condensed:wght@400;700&display=swap">
<style>
  :root {
    --bg-top: #e6e6e6;
    --bg-mid: #a9a9a9;
    --bg-low: #d4d4d4;
    --ink: #111111;
    --grey-text: #555555;
    --brand-blue: #1d6fb8;
    --brand-teal: #2aa7c9;
    --label-white: #ffffff;
    --kiwi: #4aa63f;
    --kiwi-dark: #3a8a31;
    --berry: #e8176f;
    --berry-dark: #c2125c;
    --grape: #7f3f98;
    --grape-dark: #66307d;
  }
  html, body {
    margin: 0;
    padding: 0;
    overflow: hidden;
  }
  .canvas {
    position: relative;
    width: 1200px;
    height: 1000px;
    overflow: hidden;
    background: linear-gradient(180deg, var(--bg-top) 0%, var(--bg-mid) 55%, var(--bg-low) 100%);
    font-family: "Roboto Condensed", "Arial Narrow", sans-serif;
  }

  /* Presentation header */
  .presentation-header {
    position: absolute;
    left: 40px;
    top: 58px;
    width: 260px;
  }
  .presentation-title {
    margin: 0;
    font: 700 34px/1 "Roboto Condensed", sans-serif;
    color: var(--ink);
    padding-left: 24px;
  }
  .header-kicker {
    margin: 8px 0 0 36px;
    font: 400 20px/1 "Open Sans", sans-serif;
    letter-spacing: 4px;
    color: var(--ink);
  }
  .header-brand {
    margin: 2px 0 0 14px;
    font: 700 64px/1 "Open Sans", sans-serif;
    color: var(--brand-blue);
  }
  .header-tagline {
    margin: 0 0 0 150px;
    font: 700 22px/1 "Roboto Condensed", sans-serif;
    color: var(--grey-text);
  }

  /* Flat label row */
  .label-row {
    position: absolute;
    left: 150px;
    top: 300px;
    display: flex;
    gap: 45px;
  }
  .flavour-label {
    position: relative;
    width: 270px;
    height: 600px;
    background: var(--label-white);
    box-shadow: 0 6px 18px rgba(0,0,0,0.18);
    overflow: hidden;
  }
  .label-arc {
    position: absolute;
    left: 0;
    top: 0;
    width: 270px;
    height: 90px;
  }
  .brand-mark {
    position: absolute;
    left: 46px;
    top: 150px;
    width: 20px;
    height: 20px;
    border-radius: 50%;
    background: var(--brand-blue);
  }
  .brand-name {
    position: absolute;
    left: 90px;
    top: 95px;
    height: 310px;
    writing-mode: vertical-rl;
    transform: rotate(180deg);
    font: 700 62px/1 "Roboto Condensed", sans-serif;
    color: var(--brand-blue);
    text-align: center;
    white-space: nowrap;
  }
  .splash-art {
    position: absolute;
    right: 0;
    top: 90px;
    width: 70px;
    height: 320px;
    background: linear-gradient(90deg, rgba(42,167,201,0) 0%, rgba(42,167,201,0.35) 60%, rgba(29,111,184,0.55) 100%);
  }

  /* Flavour block */
  .calorie-badge {
    position: absolute;
    left: 10px;
    top: 430px;
    width: 52px;
    height: 60px;
    border: 2px solid var(--accent);
    box-sizing: border-box;
    text-align: center;
    color: var(--accent);
  }
  .calorie-number {
    display: block;
    font: 700 28px/1 "Roboto Condensed", sans-serif;
    margin-top: 4px;
  }
  .calorie-note {
    display: block;
    font: 700 7px/1.1 "Roboto Condensed", sans-serif;
    text-transform: uppercase;
  }
  .volume {
    position: absolute;
    left: 12px;
    top: 496px;
    font: 700 13px/1 "Roboto Condensed", sans-serif;
    color: var(--accent);
  }
  .flavour-name {
    position: absolute;
    left: 68px;
    right: 0;
    top: 430px;
    height: 32px;
    margin: 0;
    background: var(--accent);
    color: var(--label-white);
    font: 700 19px/32px "Roboto Condensed", sans-serif;
    padding-left: 10px;
    letter-spacing: 0.5px;
  }
  .claim-list {
    position: absolute;
    left: 68px;
    right: 0;
    top: 462px;
    margin: 0;
    padding: 6px 0 6px 8px;
    list-style: none;
    background: var(--accent-dark);
  }
  .claim-list li {
    display: flex;
    align-items: center;
    gap: 6px;
    font: 700 10.5px/19px "Open Sans", sans-serif;
    color: rgba(255,255,255,0.88);
    white-space: nowrap;
  }
  .claim-icon {
    width: 10px;
    height: 10px;
    flex: none;
  }

  .flavour-label.kiwi { --accent: var(--kiwi); --accent-dark: var(--kiwi-dark); }
  .flavour-label.berry { --accent: var(--berry); --accent-dark: var(--berry-dark); }
  .flavour-label.grape { --accent: var(--grape); --accent-dark: var(--grape-dark); }
</style>
</head>
<body>
<main class="canvas">

  <header class="presentation-header">
    <h1 class="presentation-title">Label Design</h1>
    <p class="header-kicker">VITAMIN</p>
    <p class="header-brand">Zelbo</p>
    <p class="header-tagline">Beverage</p>
  </header>

  <section class="label-row">

    <article class="flavour-label kiwi">
      <svg class="label-arc" viewBox="0 0 270 90" aria-hidden="true">
        <path d="M0 58 Q135 -10 270 58 L270 74 Q135 6 0 74 Z" fill="var(--brand-blue)"/>
      </svg>
      <span class="brand-mark"></span>
      <p class="brand-name">Vitamin Zelbo</p>
      <div class="splash-art" role="img" aria-label="Water splash with rising bubbles"></div>
      <div class="calorie-badge">
        <span class="calorie-number">50</span>
        <span class="calorie-note">Calorie per bottle</span>
      </div>
      <span class="volume">400 ML</span>
      <h2 class="flavour-name">KIWI . STRAWBERRY</h2>
      <ul class="claim-list">
        <li><svg class="claim-icon" viewBox="0 0 10 10"><rect width="10" height="10" fill="#222"/><path d="M5 2v6M2 5h6" stroke="#fff" stroke-width="1.4"/></svg>Flavoured + Natural Flavour</li>
        <li><svg class="claim-icon" viewBox="0 0 10 10"><rect width="10" height="10" fill="#222"/><path d="M5 2v6M2 5h6" stroke="#fff" stroke-width="1.4"/></svg>No Artificial Coloring Added</li>
        <li><svg class="claim-icon" viewBox="0 0 10 10"><rect width="10" height="10" fill="#222"/><path d="M5 2v6M2 5h6" stroke="#fff" stroke-width="1.4"/></svg>Real Minirals &amp; Electrolytes</li>
      </ul>
    </article>

    <article class="flavour-label berry">
      <svg class="label-arc" viewBox="0 0 270 90" aria-hidden="true">
        <path d="M0 58 Q135 -10 270 58 L270 74 Q135 6 0 74 Z" fill="var(--brand-blue)"/>
      </svg>
      <span class="brand-mark"></span>
      <p class="brand-name">Vitamin Zelbo</p>
      <div class="splash-art" role="img" aria-label="Water splash with rising bubbles"></div>
      <div class="calorie-badge">
        <span class="calorie-number">50</span>
        <span class="calorie-note">Calorie per bottle</span>
      </div>
      <span class="volume">400 ML</span>
      <h2 class="flavour-name">KIWI . STRAWBERRY</h2>
      <ul class="claim-list">
        <li><svg class="claim-icon" viewBox="0 0 10 10"><rect width="10" height="10" fill="#222"/><path d="M5 2v6M2 5h6" stroke="#fff" stroke-width="1.4"/></svg>Flavoured + Natural Flavour</li>
        <li><svg class="claim-icon" viewBox="0 0 10 10"><rect width="10" height="10" fill="#222"/><path d="M5 2v6M2 5h6" stroke="#fff" stroke-width="1.4"/></svg>No Artificial Coloring Added</li>
        <li><svg class="claim-icon" viewBox="0 0 10 10"><rect width="10" height="10" fill="#222"/><path d="M5 2v6M2 5h6" stroke="#fff" stroke-width="1.4"/></svg>Real Minirals &amp; Electrolytes</li>
      </ul>
    </article>

    <article class="flavour-label grape">
      <svg class="label-arc" viewBox="0 0 270 90" aria-hidden="true">
        <path d="M0 58 Q135 -10 270 58 L270 74 Q135 6 0 74 Z" fill="var(--brand-blue)"/>
      </svg>
      <span class="brand-mark"></span>
      <p class="brand-name">Vitamin Zelbo</p>
      <div class="splash-art" role="img" aria-label="Water splash with rising bubbles"></div>
      <div class="calorie-badge">
        <span class="calorie-number">50</span>
        <span class="calorie-note">Calorie per bottle</span>
      </div>
      <span class="volume">400 ML</span>
      <h2 class="flavour-name">KIWI . STRAWBERRY</h2>
      <ul class="claim-list">
        <li><svg class="claim-icon" viewBox="0 0 10 10"><rect width="10" height="10" fill="#222"/><path d="M5 2v6M2 5h6" stroke="#fff" stroke-width="1.4"/></svg>Flavoured + Natural Flavour</li>
        <li><svg class="claim-icon" viewBox="0 0 10 10"><rect width="10" height="10" fill="#222"/><path d="M5 2v6M2 5h6" stroke="#fff" stroke-width="1.4"/></svg>No Artificial Coloring Added</li>
        <li><svg class="claim-icon" viewBox="0 0 10 10"><rect width="10" height="10" fill="#222"/><path d="M5 2v6M2 5h6" stroke="#fff" stroke-width="1.4"/></svg>Real Minirals &amp; Electrolytes</li>
      </ul>
    </article>

  </section>
</main>
</body>
</html>
```